luxury contemporary fashion website needs simple, elegant flowchart to describe the buying and selli

* Luxury, resale, preloved items are sold on this online platform
*Horizontal, simple, flowchart with 5 steps in 'friendly' font with a simple emoticon/ picture for each step
*To be positioned in the 'How we work' tab of the webpage to explain in a very simple manner the buying and selling process for the customers.
*Attached is a very rudimentary mock-up of what we would like included and an idea of a project similar to what we desire
* to confirm the text for each step, we have also attached a word file below

Industry/Entity Type

Fashion

Font styles to use
Sans Serif

Colors
86cfc6
cfeae6

Requirements
Must have
• Simple drawing / shape after each point In the closest to 'duck egg blue' fill colour you can find with a black outline

```html
<!DOCTYPE html>
<html lang="en">
<head>
<meta charset="utf-8">
<title>Bespoke Concierge Service – How We Work</title>
<link rel="stylesheet" href="https://fonts.googleapis.com/css2?family=Open+Sans:wght@600&family=Tinos&display=swap">
<style>
  :root {
    --duck-egg: #86cfc6;
    --duck-egg-pale: #cfeae6;
    --ink: #1a1a1a;
    --rule: #bdbdbd;
    --white: #ffffff;
  }
  * { margin: 0; padding: 0; box-sizing: border-box; }
  html, body { width: 1200px; height: 444px; overflow: hidden; background: var(--white); }
  .concierge { position: relative; width: 1200px; height: 444px; font-family: "Tinos", "Times New Roman", serif; color: var(--ink); }

  .title-rule { position: absolute; top: 58px; height: 1px; background: var(--rule); }
  .title-rule--left { left: 0; width: 300px; }
  .title-rule--right { left: 878px; right: 0; }
  .section-title {
    position: absolute; top: 32px; left: 0; width: 1200px; text-align: center;
    font-family: "Open Sans", Arial, sans-serif; font-weight: 600; font-size: 38px;
    line-height: 52px; color: var(--duck-egg); letter-spacing: -0.3px;
  }

  .step { position: absolute; top: 150px; width: 200px; margin-left: -100px; text-align: center; }
  .step-badge {
    width: 56px; height: 56px; margin: 0 auto; border-radius: 50%;
    border: 3.5px solid var(--duck-egg); display: flex; align-items: center; justify-content: center;
  }
  .step-number {
    width: 41px; height: 41px; border-radius: 50%; background: var(--duck-egg); color: var(--white);
    font-size: 19px; line-height: 41px;
  }
  .step-heading {
    width: 178px; margin: 14px auto 0; padding-bottom: 6px; border-bottom: 1px solid var(--ink);
    font-size: 15.5px; letter-spacing: 0.2px; text-transform: uppercase; white-space: nowrap;
  }
  .step-text { margin-top: 8px; font-size: 12.5px; line-height: 14px; }
  .step-icon { display: block; margin: 20px auto 0; }

  .step-split { display: flex; justify-content: center; margin-top: 8px; }
  .split-col { width: 100px; font-size: 12.5px; line-height: 14px; }
  .split-col .step-icon { margin-top: 14px; }
  .split-col--left { width: 98px; border-right: 1px solid var(--ink); padding-bottom: 8px; }
  .currency { margin-top: 12px; font-family: "Open Sans", Arial, sans-serif; font-weight: 600; font-size: 19px; color: var(--duck-egg); }

  .chevron { position: absolute; top: 162px; }

  .cta-band { position: absolute; left: 0; top: 353px; width: 1200px; height: 91px; background: var(--duck-egg-pale); }
  .cta-button {
    position: absolute; left: 461px; top: 24px; width: 273px; height: 45px; background: var(--duck-egg);
    color: var(--white); font-size: 17px; letter-spacing: 0.3px; text-decoration: none;
    display: flex; align-items: center; justify-content: center; gap: 34px; padding-left: 10px;
  }
</style>
</head>
<body>
<main class="concierge">
  <div class="title-rule title-rule--left"></div>
  <div class="title-rule title-rule--right"></div>
  <h1 class="section-title">Bespoke Concierge Service</h1>

  <section class="step" style="left:130px">
    <div class="step-badge"><span class="step-number">1</span></div>
    <h2 class="step-heading" style="font-weight:400">Have items to sell?</h2>
    <p class="step-text">Brandsparkling or nearly new.</p>
    <svg class="step-icon" width="28" height="26" viewBox="0 0 28 26" aria-hidden="true">
      <polygon fill="var(--duck-egg)" points="8,9 10.2,14 15.5,14.3 11.4,17.7 12.8,23 8,20 3.2,23 4.6,17.7 0.5,14.3 5.8,14"/>
      <polygon fill="var(--duck-egg)" points="18,1 19.1,3.6 21.8,3.8 19.7,5.5 20.4,8.2 18,6.7 15.6,8.2 16.3,5.5 14.2,3.8 16.9,3.6"/>
      <circle cx="22" cy="17" r="1.6" fill="var(--duck-egg)"/>
    </svg>
  </section>

  <svg class="chevron" width="16" height="32" viewBox="0 0 16 32" style="left:236px" aria-hidden="true"><polyline points="3,2 13,16 3,30" fill="none" stroke="var(--duck-egg-pale)" stroke-width="4"/></svg>

  <section class="step" style="left:360px">
    <div class="step-badge"><span class="step-number">2</span></div>
    <h2 class="step-heading" style="font-weight:400">Personal collection</h2>
    <p class="step-text">We choose the pieces we know<br>the velora customer will love</p>
    <svg class="step-icon" width="22" height="22" viewBox="0 0 22 22" style="margin-top:14px" aria-hidden="true">
      <path fill="var(--duck-egg)" d="M11 21 C4 15 1 11.5 1 7.5 A5 5 0 0 1 11 5 A5 5 0 0 1 21 7.5 C21 11.5 18 15 11 21Z"/>
    </svg>
  </section>

  <svg class="chevron" width="16" height="32" viewBox="0 0 16 32" style="left:482px" aria-hidden="true"><polyline points="3,2 13,16 3,30" fill="none" stroke="var(--duck-egg-pale)" stroke-width="4"/></svg>

  <section class="step" style="left:594px">
    <div class="step-badge"><span class="step-number">3</span></div>
    <h2 class="step-heading" style="font-weight:400">We prepare</h2>
    <p class="step-text">Brandsparkling or nearly new.</p>
    <svg class="step-icon" width="24" height="24" viewBox="0 0 24 24" aria-hidden="true">
      <circle cx="12" cy="12" r="11.5" fill="var(--duck-egg)"/>
      <circle cx="8.3" cy="9.5" r="1.5" fill="var(--white)"/>
      <circle cx="15.7" cy="9.5" r="1.5" fill="var(--white)"/>
      <path d="M6.8 14 Q12 19.5 17.2 14" fill="none" stroke="var(--white)" stroke-width="1.6" stroke-linecap="round"/>
    </svg>
  </section>

  <svg class="chevron" width="16" height="32" viewBox="0 0 16 32" style="left:704px" aria-hidden="true"><polyline points="3,2 13,16 3,30" fill="none" stroke="var(--duck-egg-pale)" stroke-width="4"/></svg>

  <section class="step" style="left:824px">
    <div class="step-badge"><span class="step-number">4</span></div>
    <h2 class="step-heading" style="font-weight:400">Once sold</h2>
    <p class="step-text">Brandsparkling or nearly new.</p>
    <svg class="step-icon" width="28" height="28" viewBox="0 0 28 28" aria-hidden="true">
      <g transform="rotate(-45 14 14)" fill="var(--duck-egg)">
        <rect x="3" y="12" width="22" height="4" rx="2"/>
        <polygon points="11,12 17,12 12,2 9,2"/>
        <polygon points="11,16 17,16 12,26 9,26"/>
        <polygon points="3,12 6,12 4,8 2,8"/>
        <polygon points="3,16 6,16 4,20 2,20"/>
      </g>
    </svg>
  </section>

  <svg class="chevron" width="16" height="32" viewBox="0 0 16 32" style="left:938px" aria-hidden="true"><polyline points="3,2 13,16 3,30" fill="none" stroke="var(--duck-egg-pale)" stroke-width="4"/></svg>

  <section class="step" style="left:1070px">
    <div class="step-badge"><span class="step-number">5</span></div>
    <h2 class="step-heading" style="font-weight:400">Your payment</h2>
    <div class="step-split">
      <div class="split-col split-col--left">
        <p>Pocket<br>your cash</p>
        <p class="currency">$€£</p>
      </div>
      <div class="split-col">
        <p>Donate your<br>cash to charity</p>
        <svg class="step-icon" width="24" height="30" viewBox="0 0 24 30" aria-hidden="true">
          <ellipse cx="12" cy="3" rx="6" ry="2" fill="none" stroke="var(--duck-egg)" stroke-width="1.4"/>
          <circle cx="12" cy="18" r="11" fill="var(--duck-egg)"/>
          <circle cx="8.5" cy="15.5" r="1.4" fill="var(--white)"/>
          <circle cx="15.5" cy="15.5" r="1.4" fill="var(--white)"/>
          <path d="M7.2 20 Q12 25 16.8 20" fill="none" stroke="var(--white)" stroke-width="1.5" stroke-linecap="round"/>
        </svg>
      </div>
    </div>
  </section>

  <div class="cta-band">
    <a class="cta-button" href="#">GET STARTED
      <svg width="8" height="10" viewBox="0 0 8 10" aria-hidden="true"><polygon points="0,0 8,5 0,10" fill="var(--white)"/></svg>
    </a>
  </div>
</main>
</body>
</html>
```